Commercial Real Estate

We need a business card design for a new commercial real estate business that specializes in apartment building brokerage. Not individual units but the entire complex. We find and represent the owners existing buildings and well as new buyers for those buildings. The design should convey trust, integrity, knowledge and growth. It should be easily read.

Target Market(s)

40 to 65 years old

Industry/Entity Type

Real Estate

```html
<!DOCTYPE html>
<html lang="en">
<head>
<meta charset="utf-8">
<title>Tallgate Property Investments – Business Card</title>
<link rel="stylesheet" href="https://fonts.googleapis.com/css2?family=Lato:wght@400;700;900&display=swap">
<style>
  :root {
    --teal: #5ec0be;
    --teal-deep: #4aa9a7;
    --ink: #3c4647;
    --card: #ffffff;
    --backdrop: #d9dcdc;
  }
  * { margin: 0; padding: 0; box-sizing: border-box; }
  html, body {
    width: 1200px; height: 900px; overflow: hidden;
    background: var(--backdrop);
    font-family: "Lato", Arial, sans-serif;
  }
  .business-card {
    position: absolute;
    left: 110px; top: 170px;
    width: 980px; height: 560px;
    background: var(--card);
    border-radius: 34px;
    overflow: hidden;
    box-shadow: 0 10px 30px rgba(0,0,0,.18);
  }
  .name-band {
    position: absolute; left: 0; top: 0; right: 0; height: 84px;
    background: var(--teal);
    text-align: right;
    padding: 14px 56px 0 0;
    color: #fff;
  }
  .holder-name { font-size: 30px; font-weight: 900; letter-spacing: .5px; line-height: 1; }
  .holder-role { font-size: 21px; font-weight: 400; margin-top: 4px; }
  .contact-list {
    position: absolute; right: 56px; top: 130px;
    list-style: none; text-align: right;
    font-size: 23px; color: var(--ink); line-height: 1.6;
  }
  .contact-list .label { color: var(--teal-deep); font-weight: 700; }
  .services {
    position: absolute; right: 56px; bottom: 72px;
    text-align: right; text-transform: uppercase;
  }
  .services .headline {
    font-size: 30px; font-weight: 900; color: var(--ink); line-height: 1.1;
  }
  .services .specialty {
    font-size: 25px; font-weight: 900; color: var(--teal-deep); margin-top: 4px;
  }
  .brand {
    position: absolute; left: 70px; bottom: 56px;
  }
  .brand-mark-row { display: flex; align-items: center; gap: 18px; }
  .brand-square { width: 56px; height: 56px; background: var(--teal); }
  .brand-name {
    font-size: 62px; font-weight: 900; color: var(--ink);
    letter-spacing: 2px; line-height: 1;
  }
  .brand-rule { width: 360px; height: 3px; background: var(--teal); margin: 14px 0 8px; }
  .brand-tagline {
    font-size: 24px; font-weight: 700; color: var(--ink); letter-spacing: 4px;
  }
</style>
</head>
<body>
  <section class="business-card">
    <header class="name-band">
      <div class="holder-name">YOUR NAME</div>
      <div class="holder-role">Designation</div>
    </header>

    <ul class="contact-list">
      <li><span class="label">Telephone:</span> 0400 555 012</li>
      <li><span class="label">Email:</span> support@tallgateinvest.com</li>
      <li><span class="label">Web:</span> www.tallgateinvest.com</li>
    </ul>

    <div class="services">
      <div class="headline">All types of<br>property investments</div>
      <div class="specialty">Apartment building brokerage</div>
    </div>

    <div class="brand">
      <div class="brand-mark-row">
        <div class="brand-square"></div>
        <div class="brand-name">TALLGATE</div>
      </div>
      <div class="brand-rule"></div>
      <div class="brand-tagline">Property Investments</div>
    </div>
  </section>
</body>
</html>
```